Halvern Aviation Group - "Coming Soon" Main Company Webpage

Design a main webpage that can be posted while a fully functional website is constructed. The design should be created to convey a sense of luxury and exclusivity. The main page should contain only one photo as the background. The photo I believe to show "luxury" and "Exclusivity" is listed as "Global Luxury Photo". I have included two other photos as well to aid in providing a variety of presentations.
The "Member PQTR" logo should appear somewhere on the main page but be less prevalent than the main company logo. "Coming Soon" should also appear to convey that a website is being constructed.
Tabs for the website:
- Aircraft Management
- Aircraft Sales
- Pilot Services
- Charter
- Flight Training

```html
<!DOCTYPE html>
<html lang="en">
<head>
<meta charset="utf-8">
<title>Halvern Aviation Group — Coming Soon</title>
<link href="https://fonts.googleapis.com/css2?family=Michroma&family=Roboto:wght@400&display=swap" rel="stylesheet">
<style>
  :root {
    --brand-blue: #0a5eac;
    --ink: #111418;
    --panel: rgba(248, 248, 248, 0.86);
    --rule: rgba(0, 0, 0, 0.09);
    --field: #fafafa;
    --placeholder: #9a9ea3;
    --sky-light: #ececec;
    --sky-mid: #cfd0d1;
    --sky-dark: #a9abad;
  }
  * { box-sizing: border-box; margin: 0; padding: 0; }
  html, body { width: 1200px; height: 675px; overflow: hidden; }
  body { font-family: "Michroma", sans-serif; color: var(--ink); position: relative; }

  .hero-photo {
    position: absolute; inset: 0;
    background:
      radial-gradient(ellipse at 85% 70%, #f4f4f4 0%, rgba(244,244,244,0) 45%),
      radial-gradient(ellipse at 30% 90%, var(--sky-dark) 0%, rgba(169,171,173,0) 55%),
      linear-gradient(180deg, var(--sky-light) 0%, var(--sky-mid) 60%, #bfc0c2 100%);
  }

  .side-panel {
    position: absolute; left: 0; top: 0; width: 332px; height: 675px;
    background: var(--panel);
  }
  .brand {
    position: absolute; left: 68px; top: 84px;
    color: var(--brand-blue); font-size: 15px; line-height: 1.35; letter-spacing: 0.02em;
  }
  .main-nav { position: absolute; left: 0; top: 187px; width: 310px; }
  .main-nav a {
    display: flex; align-items: center; padding-left: 68px;
    border-top: 1px solid var(--rule);
    color: var(--ink); text-decoration: none; font-size: 10px; letter-spacing: 0.02em;
    -webkit-text-stroke: 0.2px var(--ink);
  }
  .main-nav a:last-child { border-bottom: 1px solid var(--rule); }

  .membership { position: absolute; left: 116px; top: 596px; }
  .membership .label { font-family: "Roboto", sans-serif; font-size: 10px; display: block; }
  .membership .name { display: block; margin-top: 2px; font-size: 23px; line-height: 28px; color: var(--ink); }

  .content { position: absolute; left: 441px; top: 52px; }
  .headline {
    color: var(--brand-blue); font-size: 74px; line-height: 78px; font-weight: 400;
    letter-spacing: 0.01em; -webkit-text-stroke: 3.5px var(--brand-blue);
  }
  .tagline { margin-top: 16px; font-size: 13.5px; -webkit-text-stroke: 0.3px var(--ink); }
  .signup { display: flex; margin-top: 33px; height: 42px; width: 458px; }
  .signup input {
    flex: 1; border: none; background: var(--field); padding-left: 19px;
    font-family: "Michroma", sans-serif; font-size: 13.5px; color: var(--ink);
    border-radius: 2px 0 0 2px; outline: none;
  }
  .signup input::placeholder { color: var(--placeholder); }
  .signup button {
    width: 67px; border: none; background: var(--brand-blue); border-radius: 0 2px 2px 0;
    display: flex; align-items: center; justify-content: center; cursor: pointer;
  }
</style>
</head>
<body>
  <div class="hero-photo" role="img" aria-label="Private business jet parked on the apron under an overcast grey sky, seen from below its wing and rear engine"></div>

  <aside class="side-panel">
    <div class="brand">HALVERN<br>AVIATION GROUP</div>
    <nav class="main-nav">
      <a href="#" style="height:52px">AIRCRAFT MANAGEMENT</a>
      <a href="#" style="height:57px">AIRCRAFT SALES</a>
      <a href="#" style="height:53px">PILOT SERVICES</a>
      <a href="#" style="height:52px">CHARTER</a>
      <a href="#" style="height:53px">FLIGHT TRAINING</a>
    </nav>
    <div class="membership">
      <span class="label">member of</span>
      <span class="name">PQTR</span>
    </div>
  </aside>

  <main class="content">
    <h1 class="headline">COMING<br>SOON</h1>
    <p class="tagline">Sign up to be the first one to know when we launch.</p>
    <form class="signup">
      <input type="email" placeholder="Email Address" aria-label="Email Address">
      <button type="button" aria-label="Submit">
        <svg width="24" height="14" viewBox="0 0 24 14" fill="none" stroke="#fff" stroke-width="1.8">
          <path d="M0 7h22M16 1l6 6-6 6"/>
        </svg>
      </button>
    </form>
  </main>
</body>
</html>
```